Quenvo Festivals

We need a website that covers a website with reviews about different festivals all around the world. Should include a directory of festivals and artists as well as a nice overview of articles.

Should include
Homepage,
Directory over artists and a detail page for artists also linking them to
a directory over festivals and a detail page for each festival with different information boxes
A nice and clean article category view for possible use of sub categories from main article archive
A modern, clean and good article page

Target Market(s)

People from all over the world that travels to music festivals and enjoys to check information online and share good deals.

Industry/Entity Type

Festival

Requirements
Must have
• Review pages with boxes and spaces for information about festivals

```html
<!DOCTYPE html>
<html lang="en">
<head>
<meta charset="utf-8">
<title>Quenvo Festivals</title>
<link rel="stylesheet" href="https://fonts.googleapis.com/css2?family=Open+Sans:ital,wght@0,400;0,600;0,700;1,400&family=Roboto+Condensed:wght@400;700&display=swap">
<style>
:root{
  --orange:#f7941d;
  --ink:#333;
  --text:#555;
  --rule:#e3e3e3;
  --panel:#f3f3f3;
  --nav-active:#5b6068;
  --btn:#5f646b;
  --footer:#1f1f1f;
  --footer-base:#151515;
  --footer-text:#8a8a8a;
}
*{box-sizing:border-box;margin:0;padding:0}
html,body{width:1200px;height:2985px;overflow:hidden}
body{position:relative;background:#fff;font-family:"Open Sans",Arial,sans-serif;color:var(--text)}
.abs{position:absolute}

/* header */
.site-header{position:absolute;left:0;top:0;width:1200px;height:82px;background:#fff}
.brand{position:absolute;left:188px;top:22px;display:flex;align-items:center;gap:10px}
.brand-dot{width:34px;height:34px;border-radius:50%;background:var(--orange)}
.brand-name{font-weight:700;font-size:22px;color:var(--orange);letter-spacing:.5px;text-transform:uppercase}
.search-mini{position:absolute;left:644px;top:30px;width:218px;height:28px;border:1px solid #ccc;border-radius:3px;font-size:11px;color:#999;padding:6px 10px}
.search-mini svg{position:absolute;right:8px;top:7px}
.top-btn{position:absolute;top:30px;height:28px;border-radius:4px;background:var(--btn);color:#fff;font-size:10px;font-weight:600;display:flex;align-items:center;justify-content:center;text-transform:uppercase}
.top-btn.login{left:874px;width:68px}
.top-btn.register{left:954px;width:66px}

/* nav */
.main-nav{position:absolute;left:0;top:82px;width:1200px;height:40px;background:var(--orange)}
.main-nav a{position:absolute;top:0;height:40px;line-height:40px;color:#fff;font-size:10px;font-weight:700;text-decoration:none;text-transform:uppercase;transform:translateX(-50%)}
.main-nav a.current{left:228px;width:96px;text-align:center;background:var(--nav-active)}

/* hero */
.hero{position:absolute;left:0;top:122px;width:1200px;height:474px;overflow:hidden}
.hero-photo{position:absolute;inset:0;background:
  radial-gradient(ellipse at 80% 40%,#3c7a4a 0,rgba(60,122,74,0) 22%),
  radial-gradient(ellipse at 60% 20%,#c8c6cc 0,rgba(200,198,204,0) 45%),
  linear-gradient(180deg,#a9a6ae 0%,#8c7a86 45%,#6a3f4e 75%,#3e2630 100%)}
.hero-title{position:absolute;left:184px;top:150px;font-family:"Roboto Condensed",Arial,sans-serif;font-weight:700;font-size:58px;color:#111;letter-spacing:-.5px}
.hero-sub{position:absolute;left:188px;top:228px;width:390px;font-family:"Roboto Condensed",Arial,sans-serif;font-weight:700;font-size:14px;line-height:22px;color:#fff;text-transform:uppercase;text-shadow:0 1px 2px #000}
.hero-arrow{position:absolute;top:206px}

/* search */
.finder{position:absolute;left:180px;top:620px;width:842px;height:62px;border:1px solid var(--rule);background:#fff}
.finder-label{position:absolute;left:22px;top:21px;font-size:14px;font-weight:700;color:var(--orange);text-transform:uppercase}
.select{position:absolute;top:20px;height:24px;border:1px solid #bbb;border-radius:2px;font-size:10px;color:#777;padding:4px 10px;background:#fff}
.select i{position:absolute;right:2px;top:2px;width:18px;height:18px;border:1px solid #999;border-radius:2px;background:linear-gradient(#fafafa,#ddd)}
.select i svg{position:absolute;left:4px;top:5px}
.finder-btn{position:absolute;left:748px;top:18px;width:74px;height:28px;border-radius:3px;background:var(--btn);color:#fff;font-size:11px;display:flex;align-items:center;justify-content:center}

/* content column */
.section-title{font-size:16px;font-weight:700;color:var(--orange);text-transform:uppercase}
.welcome{position:absolute;left:180px;top:704px;width:540px}
.welcome p{margin-top:12px;font-size:10.5px;line-height:16px}
.bar{position:absolute;left:180px;width:540px;height:34px;background:var(--panel);padding:0 16px;display:flex;align-items:center;justify-content:space-between}
.bar h2{font-size:15px;font-weight:700;color:var(--orange);text-transform:uppercase}
.bar .pager{display:flex;gap:10px;color:#999;font-size:14px}

.grid{position:absolute;left:180px;width:540px;display:grid;grid-template-columns:254px 254px;column-gap:32px;row-gap:0}
.card{height:308px}
.thumb{height:150px}
.card h3{margin-top:16px;font-size:10px;font-weight:700;color:var(--orange);text-transform:uppercase}
.card p{margin-top:8px;font-size:10.5px;line-height:16px;color:#444}
.meta{display:flex;align-items:center;gap:10px;font-size:10px;font-style:italic;color:var(--orange)}
.card .meta{margin-top:10px;padding-top:12px;border-top:1px solid var(--rule)}
.meta .sep{color:#bbb;font-style:normal}

.video{position:absolute;overflow:hidden}
.video .play{position:absolute;left:50%;top:50%;width:60px;height:60px;margin:-30px 0 0 -30px;border-radius:50%;background:rgba(0,0,0,.35)}
.controls{position:absolute;left:0;bottom:0;width:100%;height:22px;background:rgba(20,20,20,.85)}
.btn-orange{display:inline-block;white-space:nowrap;background:var(--orange);color:#fff;font-size:8.5px;font-weight:700;text-transform:uppercase;padding:0 12px;height:22px;line-height:22px}

/* sidebar */
.side{position:absolute;left:746px;width:276px}
.cats{border:1px solid var(--rule);background:#fafafa;margin-top:14px;padding:6px 0}
.cats li{list-style:none;height:36px;line-height:36px;padding-left:36px;font-size:11px;color:#444;border-bottom:1px solid #ececec;position:relative}
.cats li:last-child{border-bottom:0}
.cats li::before{content:"";position:absolute;left:22px;top:16px;border-left:4px solid #999;border-top:3px solid transparent;border-bottom:3px solid transparent}
.mini{display:flex;gap:14px;height:102px;padding-top:14px;border-bottom:1px solid var(--rule)}
.mini .thumb{width:86px;height:68px;flex:none}
.mini h4{font-size:9.5px;font-weight:700;color:var(--orange);text-transform:uppercase}
.mini p{font-size:10px;line-height:17px;color:#444;margin-top:4px}
.mini .meta{margin-top:6px;font-size:9.5px}
.archive li{list-style:none;height:27.4px;line-height:27px;padding-left:14px;font-size:10.5px;color:#555;border-bottom:1px solid #ececec;position:relative}
.archive li::before{content:"";position:absolute;left:2px;top:11px;border-left:4px solid #aaa;border-top:3px solid transparent;border-bottom:3px solid transparent}

/* footer */
.site-footer{position:absolute;left:0;top:2708px;width:1200px;height:222px;background:var(--footer)}
.fcol{position:absolute;top:50px;width:240px;font-size:10.5px;line-height:18px;color:var(--footer-text)}
.fcol h5{font-size:13px;font-weight:400;color:#bbb;text-transform:uppercase;padding-bottom:8px;border-bottom:1px solid #333;margin-bottom:14px}
.fcol small{display:block;font-size:9.5px;color:#666;margin-bottom:8px}
.social{display:flex;gap:10px;margin-top:16px}
.social span{width:22px;height:22px;border-radius:50%;background:#555}
.footer-base{position:absolute;left:0;top:2930px;width:1200px;height:55px;background:var(--footer-base);font-size:10px;color:#777;text-align:center;line-height:55px}
.to-top{position:absolute;right:90px;top:0;color:#666;font-size:11px}
</style>
</head>
<body>

<header class="site-header">
  <div class="brand"><span class="brand-dot"></span><span class="brand-name">Quenvo Festivals</span></div>
  <div class="search-mini">Search :
    <svg width="14" height="14" viewBox="0 0 14 14"><circle cx="6" cy="6" r="4.5" fill="none" stroke="#999" stroke-width="1.5"/><line x1="9.3" y1="9.3" x2="13" y2="13" stroke="#999" stroke-width="1.8"/></svg>
  </div>
  <div class="top-btn login">Login</div>
  <div class="top-btn register">Register</div>
</header>

<nav class="main-nav">
  <a class="current" href="#">Home</a>
  <a href="#" style="left:330px">About us</a>
  <a href="#" style="left:438px">Updates</a>
  <a href="#" style="left:544px">Articles</a>
  <a href="#" style="left:660px">Categories</a>
  <a href="#" style="left:770px">Reviews</a>
  <a href="#" style="left:866px">Blog</a>
  <a href="#" style="left:962px">Videos</a>
</nav>

<section class="hero">
  <div class="hero-photo" role="img" aria-label="Festival crowd covered in coloured powder in front of a domed palace, a reveller on shoulders with arm raised"></div>
  <h1 class="hero-title">QUENVO FESTIVAL</h1>
  <p class="hero-sub">Covers reviews about different festivals all around the world. Should include a directory of festivals and artists as well as a nice overview of articles.</p>
  <svg class="hero-arrow" style="left:76px" width="50" height="50" viewBox="0 0 50 50"><circle cx="25" cy="25" r="23" fill="rgba(255,255,255,.25)" stroke="rgba(255,255,255,.6)" stroke-width="2"/><polyline points="29,15 19,25 29,35" fill="none" stroke="#fff" stroke-width="3"/></svg>
  <svg class="hero-arrow" style="left:1076px" width="50" height="50" viewBox="0 0 50 50"><circle cx="25" cy="25" r="23" fill="rgba(255,255,255,.25)" stroke="rgba(255,255,255,.6)" stroke-width="2"/><polyline points="21,15 31,25 21,35" fill="none" stroke="#fff" stroke-width="3"/></svg>
</section>

<form class="finder">
  <span class="finder-label">Search festivals and artists</span>
  <div class="select" style="left:258px;width:226px">Country :<i><svg width="10" height="7" viewBox="0 0 10 7"><polygon points="0,0 10,0 5,7" fill="#555"/></svg></i></div>
  <div class="select" style="left:496px;width:238px">City :<i><svg width="10" height="7" viewBox="0 0 10 7"><polygon points="0,0 10,0 5,7" fill="#555"/></svg></i></div>
  <div class="finder-btn">Search</div>
</form>

<!-- main column -->
<section class="welcome">
  <h2 class="section-title">Welcome to Quenvo Festival</h2>
  <p>It is a long established fact that a reader will be distracted by the readable content of a page when looking at its layout. The point of using Lorem Ipsum is that it has a more-or-less normal distribution of letters, as opposed to using 'Content here, content here', making it look like readable English...</p>
</section>

<div class="bar" style="top:818px"><h2>Artists</h2><span class="pager">‹ ›</span></div>
<div class="grid" style="top:876px">
  <article class="card"><div class="thumb" role="img" aria-label="Dancers throwing pink and yellow colour powder" style="background:linear-gradient(135deg,#e86aa0,#f2a24a 55%,#d34c7a)"></div><h3>Publishing packages</h3><p>It is a long established fact that a reader will be distracted by the readable content of a page when looking at its layout. The point of using...</p><div class="meta">Posted on 24 Jun 2013 <span class="sep">|</span> <svg width="10" height="9" viewBox="0 0 10 9"><path d="M0 0h10v6H4L1 9V6H0z" fill="#999"/></svg> Comments</div></article>
  <article class="card"><div class="thumb" role="img" aria-label="Performer in a feathered carnival headdress" style="background:linear-gradient(135deg,#f0b030,#c8401e 50%,#5a2a1a)"></div><h3>Publishing packages</h3><p>It is a long established fact that a reader will be distracted by the readable content of a page when looking at its layout. The point of using...</p><div class="meta">Posted on 24 Jun 2013 <span class="sep">|</span> <svg width="10" height="9" viewBox="0 0 10 9"><path d="M0 0h10v6H4L1 9V6H0z" fill="#999"/></svg> Comments</div></article>
  <article class="card"><div class="thumb" role="img" aria-label="Floating lanterns glowing on a lake at night" style="background:radial-gradient(circle at 50% 70%,#d88a2a,#3a2a1a 55%,#0d1a2c)"></div><h3>Publishing packages</h3><p>It is a long established fact that a reader will be distracted by the readable content of a page when looking at its layout. The point of using...</p><div class="meta">Posted on 24 Jun 2013 <span class="sep">|</span> <svg width="10" height="9" viewBox="0 0 10 9"><path d="M0 0h10v6H4L1 9V6H0z" fill="#999"/></svg> Comments</div></article>
  <article class="card"><div class="thumb" role="img" aria-label="Traditional dancers in red costumes on a night stage" style="background:linear-gradient(180deg,#1a1512,#6a3a26 60%,#a8542e)"></div><h3>Publishing packages</h3><p>It is a long established fact that a reader will be distracted by the readable content of a page when looking at its layout. The point of using...</p><div class="meta">Posted on 24 Jun 2013 <span class="sep">|</span> <svg width="10" height="9" viewBox="0 0 10 9"><path d="M0 0h10v6H4L1 9V6H0z" fill="#999"/></svg> Comments</div></article>
</div>

<div class="bar" style="top:1490px"><h2>Video player</h2><span class="pager">‹ ›</span></div>
<div class="video" style="left:180px;top:1548px;width:540px;height:326px">
  <div role="img" aria-label="Festival crowd cheering in the sun with flags overhead" style="position:absolute;inset:0;background:linear-gradient(180deg,#9cb07a 0%,#7b7f62 30%,#8c6a52 65%,#4a3a30 100%)"></div>
  <div class="play"></div>
  <div class="controls"><svg width="540" height="22" viewBox="0 0 540 22"><polygon points="12,6 12,16 20,11" fill="#fff"/><rect x="32" y="9" width="400" height="4" fill="#555"/><rect x="32" y="9" width="60" height="4" fill="#aaa"/><rect x="444" y="7" width="6" height="8" fill="#ccc"/><polygon points="450,7 456,3 456,19 450,15" fill="#ccc"/></svg></div>
</div>
<div class="abs" style="left:180px;top:1894px;width:540px">
  <h3 style="font-size:12px;font-weight:700;color:var(--orange);text-transform:uppercase">Contrary to popular belief</h3>
  <p style="margin-top:10px;font-size:10px;line-height:16px;color:#444">It is a long established fact that a reader will be distracted by the readable content of a page when looking at its layout. The point of using it is a long established fact that a reader will be distracted by the readable content of a page when looking at its layout. The point of using it is a long established fact that a reader will be distracted...</p>
  <span class="btn-orange" style="margin-top:14px">View more videos</span>
</div>

<div class="bar" style="top:2030px"><h2>Festivals</h2><span class="pager">‹ ›</span></div>
<div class="grid" style="top:2084px">
  <article class="card"><div class="thumb" role="img" aria-label="Reveller laughing under bright colour powder" style="background:linear-gradient(135deg,#2a8a4a,#e0c030 45%,#d0306a)"></div><h3>Publishing packages</h3><p>It is a long established fact that a reader will be distracted by the readable content of a page when looking at its layout. The point of using...</p><div class="meta">Posted on 24 Jun 2013 <span class="sep">|</span> <svg width="10" height="9" viewBox="0 0 10 9"><path d="M0 0h10v6H4L1 9V6H0z" fill="#999"/></svg> Comments</div></article>
  <article class="card"><div class="thumb" role="img" aria-label="Figure carrying an offering into the sea" style="background:linear-gradient(180deg,#8fc4d8,#3d8aa8 50%,#1c5470)"></div><h3>Publishing packages</h3><p>It is a long established fact that a reader will be distracted by the readable content of a page when looking at its layout. The point of using...</p><div class="meta">Posted on 24 Jun 2013 <span class="sep">|</span> <svg width="10" height="9" viewBox="0 0 10 9"><path d="M0 0h10v6H4L1 9V6H0z" fill="#999"/></svg> Comments</div></article>
  <article class="card"><div class="thumb" role="img" aria-label="Packed crowd dancing with arms raised" style="background:linear-gradient(135deg,#c8a080,#8a5a40 50%,#3a2418)"></div><h3>Publishing packages</h3><p>It is a long established fact that a reader will be distracted by the readable content of a page when looking at its layout. The point of using...</p><div class="meta">Posted on 24 Jun 2013 <span class="sep">|</span> <svg width="10" height="9" viewBox="0 0 10 9"><path d="M0 0h10v6H4L1 9V6H0z" fill="#999"/></svg> Comments</div></article>
  <article class="card"><div class="thumb" role="img" aria-label="Rows of lit oil lamps glowing orange" style="background:radial-gradient(circle at 40% 50%,#ffb040,#d0501a 50%,#4a1408)"></div><h3>Publishing packages</h3><p>It is a long established fact that a reader will be distracted by the readable content of a page when looking at its layout. The point of using...</p><div class="meta">Posted on 24 Jun 2013 <span class="sep">|</span> <svg width="10" height="9" viewBox="0 0 10 9"><path d="M0 0h10v6H4L1 9V6H0z" fill="#999"/></svg> Comments</div></article>
</div>

<!-- sidebar -->
<aside class="side" style="top:702px">
  <h2 class="section-title">Categories</h2>
  <ul class="cats"><li>USA</li><li>Europa</li><li>Africa</li><li>Australia</li><li>Popular</li><li>Trending</li></ul>
</aside>

<aside class="side" style="top:980px">
  <h2 class="section-title">Recent videos</h2>
  <div class="video" style="position:relative;margin-top:16px;width:276px;height:204px">
    <div role="img" aria-label="Festival goers splashing in red powder" style="position:absolute;inset:0;background:linear-gradient(135deg,#c85a6a,#a0283a 55%,#6a1a24)"></div>
    <div class="play" style="width:44px;height:44px;margin:-22px 0 0 -22px"></div>
    <div class="controls" style="height:18px;background:#e6e6e6"><svg width="276" height="18" viewBox="0 0 276 18"><polygon points="8,5 8,13 14,9" fill="#333"/><text x="20" y="12" font-size="7" fill="#333" font-family="Open Sans,sans-serif">00:00</text><rect x="46" y="8" width="140" height="3" fill="#aaa"/><text x="192" y="12" font-size="7" fill="#333" font-family="Open Sans,sans-serif">00:00</text><rect x="220" y="6" width="4" height="6" fill="#333"/><polygon points="224,6 228,3 228,15 224,12" fill="#333"/><rect x="250" y="5" width="8" height="8" fill="none" stroke="#333"/></svg></div>
  </div>
  <p style="margin-top:14px;font-size:10px;line-height:16px;color:#444">It is a long established fact that a reader will be distracted by the readable content of a page when looking at its layout. The point of using Lorem Ipsum is that it has a more...</p>
  <span class="btn-orange" style="margin-top:14px">View more videos</span>
</aside>

<aside class="side" style="top:1356px">
  <h2 class="section-title">Most visited</h2>
  <div class="mini"><div class="thumb" role="img" aria-label="Crowd at a night concert" style="background:linear-gradient(135deg,#7a5a3a,#3a2a1e)"></div><div><h4>Contrary to popular belby</h4><p>Contrary to popular belief, Lorem Ipsum is not simply random text.</p><div class="meta">Posted on 24 Jun 2013 <span class="sep">|</span> Comments</div></div></div>
  <div class="mini"><div class="thumb" role="img" aria-label="Dancers in colourful dress" style="background:linear-gradient(135deg,#d88a5a,#8a3a2a)"></div><div><h4>Contrary to popular belby</h4><p>Contrary to popular belief, Lorem Ipsum is not simply random text.</p><div class="meta">Posted on 24 Jun 2013 <span class="sep">|</span> Comments</div></div></div>
  <div class="mini"><div class="thumb" role="img" aria-label="Crowd throwing colour powder" style="background:linear-gradient(135deg,#c86a8a,#7a3a4a)"></div><div><h4>Contrary to popular belby</h4><p>Contrary to popular belief, Lorem Ipsum is not simply random text.</p><div class="meta">Posted on 24 Jun 2013 <span class="sep">|</span> Comments</div></div></div>
  <span class="btn-orange" style="margin-top:16px">View more post</span>
</aside>

<aside class="side" style="top:1746px">
  <h2 class="section-title">Popular posts</h2>
  <div class="mini"><div class="thumb" role="img" aria-label="Festival crowd at dusk" style="background:linear-gradient(135deg,#8a6a4a,#3a281a)"></div><div><h4>Contrary to popular belby</h4><p>Contrary to popular belief, Lorem Ipsum is not simply random text.</p><div class="meta">Posted on 24 Jun 2013 <span class="sep">|</span> Comments</div></div></div>
  <div class="mini"><div class="thumb" role="img" aria-label="Colour powder celebration" style="background:linear-gradient(135deg,#e08a9a,#a04a5a)"></div><div><h4>Contrary to popular belby</h4><p>Contrary to popular belief, Lorem Ipsum is not simply random text.</p><div class="meta">Posted on 24 Jun 2013 <span class="sep">|</span> Comments</div></div></div>
  <div class="mini"><div class="thumb" role="img" aria-label="Revellers dusted in pink powder" style="background:linear-gradient(135deg,#d07aa0,#8a3a5a)"></div><div><h4>Contrary to popular belby</h4><p>Contrary to popular belief, Lorem Ipsum is not simply random text.</p><div class="meta">Posted on 24 Jun 2013 <span class="sep">|</span> Comments</div></div></div>
  <span class="btn-orange" style="margin-top:16px">View more post</span>
</aside>

<aside class="side" style="top:2132px">
  <h2 class="section-title">Archive</h2>
  <ul class="archive" style="margin-top:10px">
    <li>November 2013</li><li>October 2013</li><li>September 2013</li><li>August 2013</li><li>July 2013</li><li>June 2013</li><li>May 2013</li><li>April 2013</li><li>March 2013</li><li>February 2013</li><li>January 2013</li>
  </ul>
</aside>

<footer class="site-footer">
  <div class="fcol" style="left:196px"><h5>About us</h5>Lorem ipsum dolor sit amet, consectetur adipiscing elit. Nulla in purus nibh. Donec ornare felis neque. Nullam tortor nulla, sodales quis posuere quis, tristique nec libero. Proin vitae convallis odio. Morbi nec enim nisl. Aliquam erat volutpat.</div>
  <div class="fcol" style="left:492px"><h5>Chirp feed</h5>Check out th best Themes online in the world at http://quenvo-demo.com<small>1 day ago</small>@marketvale, Tempra site theme full responsive is coming soon...<small>4 days ago</small></div>
  <div class="fcol" style="left:788px"><h5>Follow us</h5>Lorem ipsum dolor sit amet, consectetur adipiscing elit. Nulla in purus nibh. Donec ornare felis neque. Nullam tortor nulla...
    <div class="social"><span></span><span></span><span></span><span></span><span></span></div>
  </div>
</footer>
<div class="footer-base">Copyright @ 2013 Quenvo Festival. All rights reserved.<span class="to-top">▲</span></div>

</body>
</html>
```